Pemberton Dialworks Business Card Design

Double Sided Business Card Design for a Locksmith company specializing in Safecracking, safe & vault service.

```html
<!DOCTYPE html>
<html lang="en">
<head>
<meta charset="utf-8">
<title>Pemberton Dialworks Business Card</title>
<link rel="stylesheet" href="https://fonts.googleapis.com/css2?family=Open+Sans:wght@400;600;700;800&display=swap">
<style>
  :root {
    --bg: #1c1c1e;
    --card-white: #ffffff;
    --card-dark: #2a2a2c;
    --green: #4c9a5c;
    --ink: #2b2b2b;
    --grey-text: #555555;
    --band-light: #d6d6d6;
    --band-mid: #8c8c8c;
    --band-dark: #5e5e5e;
    --emboss: #3d3d40;
  }
  * { margin: 0; padding: 0; box-sizing: border-box; }
  html, body { width: 1200px; height: 900px; overflow: hidden; }
  body {
    background: var(--bg);
    font-family: "Open Sans", sans-serif;
    position: relative;
  }
  .card {
    position: absolute;
    left: 250px;
    width: 700px;
    height: 400px;
    border-radius: 22px;
    overflow: hidden;
  }
  .card--front { top: 40px; background: var(--card-white); }
  .card--back { top: 460px; background: var(--card-dark); }

  .swoosh { position: absolute; inset: 0; width: 700px; height: 400px; }

  .contact-block { position: absolute; left: 48px; top: 60px; }
  .person-name {
    color: var(--green);
    font-weight: 800;
    font-size: 22px;
    letter-spacing: 0.5px;
    text-transform: uppercase;
  }
  .person-title {
    color: var(--grey-text);
    font-size: 16px;
    margin-top: 2px;
  }
  .contact-list { list-style: none; margin-top: 22px; }
  .contact-item {
    display: flex;
    align-items: center;
    gap: 10px;
    font-size: 16px;
    color: var(--ink);
    line-height: 26px;
  }
  .contact-item svg { width: 14px; height: 14px; flex: none; }
  .contact-item--web { color: var(--green); }

  .brand {
    position: absolute;
    display: flex;
    align-items: center;
    gap: 14px;
  }
  .card--front .brand { right: 60px; top: 180px; }
  .brand-dot {
    width: 34px; height: 34px; border-radius: 50%;
    background: var(--green);
    flex: none;
  }
  .brand-name {
    font-weight: 800;
    font-size: 30px;
    line-height: 1.05;
    text-transform: uppercase;
    color: var(--ink);
    letter-spacing: 0.5px;
  }
  .card--back .brand {
    left: 50%; top: 50%;
    transform: translate(-50%, -50%);
  }
  .card--back .brand-dot { background: var(--emboss); width: 56px; height: 56px; }
  .card--back .brand-name { color: var(--emboss); font-size: 46px; }
</style>
</head>
<body>
  <section class="card card--front">
    <svg class="swoosh" viewBox="0 0 700 400" aria-hidden="true">
      <path d="M0,215 C140,270 360,330 545,400 L0,400 Z" fill="var(--band-light)"/>
      <path d="M0,238 C150,292 350,338 515,400 L0,400 Z" fill="var(--band-mid)"/>
      <path d="M0,268 C150,314 330,352 470,400 L0,400 Z" fill="var(--band-dark)"/>
      <path d="M270,316 C385,322 475,352 545,400 L528,400 C462,360 380,330 270,316 Z" fill="var(--green)"/>
    </svg>

    <div class="contact-block">
      <h1 class="person-name">Marcus R. Linwood</h1>
      <p class="person-title">Co-Founder &amp; Partner</p>
      <ul class="contact-list">
        <li class="contact-item">
          <svg viewBox="0 0 24 24"><path fill="var(--green)" d="M6.6 10.8a15.1 15.1 0 0 0 6.6 6.6l2.2-2.2c.3-.3.7-.4 1-.2 1.1.4 2.3.6 3.6.6.6 0 1 .4 1 1V20c0 .6-.4 1-1 1A17 17 0 0 1 3 4c0-.6.4-1 1-1h3.5c.6 0 1 .4 1 1 0 1.3.2 2.5.6 3.6.1.3 0 .7-.2 1z"/></svg>
          (214) 555-0143
        </li>
        <li class="contact-item">
          <svg viewBox="0 0 24 24"><path fill="var(--green)" d="M2 5h20v14H2z"/><path d="M2 5l10 8 10-8" fill="none" stroke="#fff" stroke-width="2"/></svg>
          Marcus@pembertondialworks.com
        </li>
        <li class="contact-item contact-item--web">
          <svg viewBox="0 0 24 24"><circle cx="12" cy="12" r="10" fill="var(--green)"/><path d="M2 12h20M12 2c3 3 3 17 0 20M12 2c-3 3-3 17 0 20" fill="none" stroke="#fff" stroke-width="1.5"/></svg>
          pembertondialworks.com
        </li>
      </ul>
    </div>

    <div class="brand">
      <span class="brand-dot"></span>
      <span class="brand-name">Pemberton<br>Dialworks</span>
    </div>
  </section>

  <section class="card card--back">
    <div class="brand">
      <span class="brand-dot"></span>
      <span class="brand-name">Pemberton<br>Dialworks</span>
    </div>
  </section>
</body>
</html>
```